IT supplier clean wordpress website - payment guaranteed

Clean website design for a wordpress based website
Design only - PSD delivery with images

current website: www.quilmo.net
please use your imagination and try something out of the box...
We like https://trevanly.com.au as look and feel, but you don't have to copy it, you can be creative

We like the navigation header and the phone number, but do not need 'instant quote' so the 1300 phone number and the 'lock' icon for login can be on the same line

Site Map:
IT support
VoIP
Internet and Data
Cloud hosting
About
Contact

Our logo is attached, it can be used light or dark.
Our only color used is the warm grey Pantone 8003C hex #877A69

You will only need to design the homepage to win the competition, but the winning designer will be required to supply without extra charges:
1. Home page design
2. A second, standard page template design
3. An icon set in colors appropriate to the site that have icons to match the subjects in these pages:
https://trevanly.com.au/products/
https://trevanly.com.au/making-the-switch/
https://trevanly.com.au/why-trevanly/
We will create a single page version of the options on https://trevanly.com.au/solutions/
4.Any images used

Please avoid stock photos that are too common - e.g. smiling woman with headset, try to make the design stand out with simple images and well-designed layout.

Mid-size business clients

It Company

1 page

• Quil logo
• Use Quil color

```html
<!DOCTYPE html>
<html lang="en">
<head>
<meta charset="utf-8">
<title>Quil — Services</title>
<link href="https://fonts.googleapis.com/css2?family=Raleway:wght@300;400;500&display=swap" rel="stylesheet">
<style>
:root{
  --warm-grey:#877A69;
  --accent:#e07b00;
  --paper:#ffffff;
  --mist:#f2f0ee;
  --earth:#4a3d30;
  --foot-head:#d9cfc3;
  --foot-link:#a99c8b;
  --body-text:#7d7062;
}
*{margin:0;padding:0;box-sizing:border-box}
html,body{width:1200px;height:1200px;overflow:hidden}
body{font-family:'Raleway',sans-serif;background:var(--paper);position:relative;color:var(--body-text)}
.top-band{position:absolute;left:0;top:0;width:1200px;height:28px;background:var(--mist)}
.section-title{position:absolute;left:0;width:100%;text-align:center;font-weight:400;color:var(--warm-grey);font-size:30px}
.divider{position:absolute;height:14px}
.divider::before{content:"";position:absolute;left:0;right:0;top:7px;border-top:1px solid var(--warm-grey)}
.divider::after{content:"";position:absolute;left:50%;top:0;width:14px;height:14px;margin-left:-7px;border:2px solid var(--accent);background:inherit}
.services .section-title{top:86px}
.services .divider{top:127px;left:562px;width:163px;background:var(--paper)}
.service{position:absolute;top:214px;width:210px}
.service-icon{width:105px;height:109px;border:2px solid var(--warm-grey);border-radius:10px;position:relative;display:flex;align-items:center;justify-content:center}
.service-icon span{width:56px;height:56px;border-radius:10px;background:var(--warm-grey);display:block}
.service h3{font-weight:400;color:var(--accent);font-size:15px;margin-top:10px}
.service p{font-weight:300;font-size:11.5px;line-height:13.6px;margin-top:10px;color:var(--body-text)}
.certified{position:absolute;left:0;top:501px;width:1200px;height:336px;background:var(--mist)}
.certified .section-title{top:28px;left:0;padding-left:28px}
.certified .divider{top:68px;left:508px;width:299px;background:var(--mist)}
.certified .lead{position:absolute;top:120px;left:134px;width:1010px;font-size:15px;font-weight:400;color:var(--warm-grey);white-space:nowrap}
.badge{position:absolute;top:197px;height:80px;border-radius:6px}
.badge.b1{left:342px;width:108px;background:#e4e4e2}
.badge.b2{left:542px;width:88px;border:2px solid #9c9c9c;background:#f6f6f6}
.badge.b3{left:747px;width:78px;background:#1f4f5c}
.footer{position:absolute;left:0;top:869px;width:1200px;height:331px;background:var(--earth)}
.foot-col{position:absolute;top:60px}
.foot-col h4{font-size:13px;font-weight:500;color:var(--foot-head);letter-spacing:.2px;margin-bottom:6px}
.foot-col a{display:block;font-size:13px;font-weight:300;color:var(--foot-link);text-decoration:none;line-height:24px}
.brand{position:absolute;left:1022px;top:46px}
.brand-mark{display:flex;align-items:center;gap:10px;margin-left:4px;margin-bottom:34px}
.brand-mark i{width:22px;height:22px;border:2px solid var(--foot-link);display:block}
.brand-mark b{font-weight:300;font-size:30px;color:var(--foot-link)}
.brand p{font-size:13px;font-weight:300;color:var(--foot-link);line-height:24px}
</style>
</head>
<body>
<div class="top-band"></div>

<section class="services">
  <h2 class="section-title">Our Services</h2>
  <div class="divider"></div>

  <div class="service" style="left:93px">
    <div class="service-icon" style="margin-left:16px" role="img" aria-label="Support agent icon"><span></span></div>
    <h3 style="margin-left:31px">IT Support</h3>
    <p>We speak many languages including plain English, and will make your experience a pleasure from start to finish.</p>
  </div>
  <div class="service" style="left:363px">
    <div class="service-icon" style="margin-left:34px" role="img" aria-label="Cloud telephone icon"><span></span></div>
    <h3 style="margin-left:69px">VoIP</h3>
    <p>We supplies a wide range of business data connections which are reliable, scalable, fast and represent excellent value for money.</p>
  </div>
  <div class="service" style="left:651px">
    <div class="service-icon" style="margin-left:19px" role="img" aria-label="Secure database icon"><span></span></div>
    <h3 style="margin-left:20px">Internet and Data</h3>
    <p>We are specialists in Corvane, fully conversant with Lumex and Ostrix. We write websites and applications.</p>
  </div>
  <div class="service" style="left:939px">
    <div class="service-icon" style="margin-left:8px" role="img" aria-label="Cloud document icon"><span></span></div>
    <h3 style="margin-left:16px">Cloud Hosting</h3>
    <p>Quil provides a range of cloud services, including Software as a service, Infrastructure as a service and Platform as a service.</p>
  </div>
</section>

<section class="certified">
  <h2 class="section-title">Certified Technicians</h2>
  <div class="divider"></div>
  <p class="lead">Be confident that the skills required are available and certified - we have a broad range of expertise and continuously update our skills and certifications</p>
  <div class="badge b1" role="img" aria-label="Certification badge"></div>
  <div class="badge b2" role="img" aria-label="Certification badge"></div>
  <div class="badge b3" role="img" aria-label="Certification badge"></div>
</section>

<footer class="footer">
  <nav class="foot-col" style="left:162px">
    <h4>COMPANY</h4>
    <a href="#">About Us</a><a href="#">Careers</a><a href="#">Legal Terms</a><a href="#">Terms of Use</a><a href="#">Privacy Policy</a>
  </nav>
  <nav class="foot-col" style="left:377px">
    <h4>SERVICES</h4>
    <a href="#">IT Support</a><a href="#">VoIP</a><a href="#">Internet and Data</a><a href="#">Cloud hosting</a>
  </nav>
  <nav class="foot-col" style="left:616px">
    <h4>PRODUCTS</h4>
    <a href="#">Corporate Workstations</a><a href="#">Orbin desktops, laptops and tablets</a><a href="#">Halvorn Standalone and Blade Servers</a><a href="#">Halvorn and Pressa Printers</a><a href="#">Maintenance Contracts</a>
  </nav>
  <div class="brand">
    <div class="brand-mark"><i></i><b>quil</b></div>
    <p>Copyright © 2017</p>
    <p>All Rights Reserved.</p>
  </div>
</footer>
</body>
</html>
```